University Social app needs Instagram layout help - tile layout and designs for 18 different types

We need a instagram profile look for our app TrelvoHub that is getting a new look and feel. We want 18 different tiles designs that mesh well and look good together on the profile page. This can be a mix of images and text. TrelvoHub is based in Sydney, Australia and is a Social app that helps students connect IRL ,find new friends and activities/experiences through society campus events. Topics can include but not limited to the following: Whats on, society spotlight, how to use TrelvoHub, TrelvoHub features, memes, Helpful hits, POV, Uni Life IRL, Make the Connection, Try Something New, TrelvoHub Community, Student Voice, Uni 101, TrelvoHub It, Student Stories. please also see current TrelvoHub instagram page for content type ideas. It also needs to have the new TrelvoHub brand colours (#04ccd9 with a gradient to white background) (also see attached file). The final tiles should communicate university fun, connection and a place to find events. Swap out the current stickers for activity based stickers similar to the attached examples to demonstrate that the app is for finding fun events and activities and for connection.
Look and feel
Each slider illustrates characteristics of the customer's brand and the style your logo design should communicate.

```html
<!DOCTYPE html>
<html lang="en">
<head>
<meta charset="UTF-8">
<title>Helpful Hits</title>
<link rel="stylesheet" href="https://fonts.googleapis.com/css2?family=Lexend:wght@600&display=swap">
<style>
  :root {
    --frame: #323945;
    --paper: #ffffff;
    --cyan: #6af8f8;
    --brush: #c9f7f8;
    --ink: #000000;
    --sun: #ffe000;
    --heart: #ff5449;
    --melon: #f25a4a;
    --eyes: #6fd0f7;
    --mint: #b2dbd8;
    --teal: #4a9198;
    --plum: #3a2070;
  }
  html, body {
    margin: 0;
    padding: 0;
    overflow: hidden;
  }
  .canvas {
    position: relative;
    width: 1200px;
    height: 1200px;
    background: var(--frame);
    overflow: hidden;
  }
  .tile {
    position: absolute;
    left: 125px;
    top: 125px;
    width: 950px;
    height: 950px;
    background: var(--paper);
    overflow: hidden;
  }
  .corner-block {
    position: absolute;
    left: 0;
    top: 0;
    width: 133px;
    height: 147px;
    background: var(--cyan);
  }
  .art {
    position: absolute;
    left: 0;
    top: 0;
    width: 950px;
    height: 950px;
  }
  .title-line {
    position: absolute;
    margin: 0;
    font-family: "Lexend", "Poppins", sans-serif;
    font-weight: 600;
    font-size: 136px;
    line-height: 1;
    letter-spacing: -3px;
    color: var(--ink);
    white-space: nowrap;
  }
  .title-line--first { left: 107px; top: 108px; }
  .title-line--second { left: 199px; top: 226px; }
  .sticker {
    position: absolute;
  }
  .sticker--heart {
    left: 599px; top: 143px; width: 140px; height: 112px;
    background: var(--heart);
    border-radius: 50% 50% 45% 45%;
  }
  .sticker--melon {
    left: 55px; top: 235px; width: 124px; height: 140px;
    background: linear-gradient(160deg, var(--melon) 70%, #00c462 70%);
    border-radius: 12px;
  }
  .sticker--eyes {
    left: 49px; top: 737px; width: 158px; height: 160px;
    background: var(--eyes);
    border-radius: 50%;
  }
  .half-disc {
    position: absolute;
    left: 225px; top: 735px;
    width: 64px; height: 128px;
    background: var(--mint);
    border-radius: 64px 0 0 64px;
  }
  .teal-block {
    position: absolute;
    left: 216px; top: 889px;
    width: 121px; height: 70px;
    background: var(--teal);
    border-radius: 8px 8px 0 0;
  }
  .plum-dome {
    position: absolute;
    left: 756px; top: 885px;
    width: 130px; height: 130px;
    background: var(--plum);
    border-radius: 50%;
  }
</style>
</head>
<body>
<div class="canvas">
  <div class="tile">
    <div class="corner-block"></div>

    <svg class="art" viewBox="0 0 950 950" aria-hidden="true">
      <g class="title-highlight" stroke="var(--brush)" stroke-linecap="round" fill="none">
        <path d="M120 150 L630 120" stroke-width="26"/>
        <path d="M90 190 L650 160" stroke-width="34"/>
        <path d="M80 235 L660 205" stroke-width="36"/>
        <path d="M75 280 L640 250" stroke-width="36"/>
        <path d="M70 320 L620 300" stroke-width="30"/>
        <path d="M90 355 L630 340" stroke-width="22"/>
      </g>
      <g class="sun-rays" stroke="var(--sun)" stroke-width="14" stroke-linecap="round">
        <path d="M731 65 L711 143"/>
        <path d="M823 95 L747 149"/>
        <path d="M763 183 L835 201"/>
      </g>
      <g class="pointer-arrow" stroke="var(--sun)" stroke-width="10" fill="none" stroke-linecap="round" stroke-linejoin="round">
        <path d="M76 282 C45 350 50 440 102 492"/>
        <path d="M55 480 L104 496 L97 453"/>
      </g>
      <g class="writing-lines" fill="var(--ink)">
        <path d="M152 471 C360 455 640 448 860 452 C868 452 869 462 860 463 C640 462 370 470 162 488 C150 489 148 476 158 477 C300 468 150 475 152 471 Z"/>
        <path d="M152 595 C360 579 640 572 860 576 C868 576 869 586 860 587 C640 586 370 594 162 612 C150 613 148 600 158 601 C300 592 150 599 152 595 Z"/>
        <path d="M152 719 C360 703 640 696 860 700 C868 700 869 710 860 711 C640 710 370 718 162 736 C150 737 148 724 158 725 C300 716 150 723 152 719 Z"/>
      </g>
    </svg>

    <h1 class="title-line title-line--first">Helpful</h1>
    <p class="title-line title-line--second">Hits</p>

    <div class="sticker sticker--heart" role="img" aria-label="Cheerful red heart sticker"></div>
    <div class="sticker sticker--melon" role="img" aria-label="Smiling watermelon slice sticker"></div>
    <div class="sticker sticker--eyes" role="img" aria-label="Pair of cartoon eyes sticker"></div>

    <div class="half-disc"></div>
    <div class="teal-block"></div>
    <div class="plum-dome"></div>
  </div>
</div>
</body>
</html>
```